Optometric Practice needs Initial Photoshop Mockup

We need a graphic design for the homepage of a website for an optometric practice that specializes in vision therapy.

Here's the link to the project folder on Filecove. I've included photos, example sites, content and instructions.

https://www.filecove.net/sh/qk7tmd3wz8rb2n5/BBX_HrLpVaQyJk6mTcDRZeNu

Please feel free to submit any questions about the design. I'll be happy to help guide you in any areas you're uncertain of.

Okay - I've updated the project to payment confirmed. Let's see some designs :) Thanks, Wes

```html
<!DOCTYPE html>
<html lang="en">
<head>
<meta charset="utf-8">
<title>Clearpath Vision Centers – Home</title>
<link href="https://fonts.googleapis.com/css2?family=Open+Sans:ital,wght@0,400;0,600;0,700;1,400;1,600&display=swap" rel="stylesheet">
<style>
:root{
  --navy:#1b1f5e;
  --maroon:#8e1b1b;
  --red:#a8141a;
  --link:#a3161c;
  --text:#2b2b2b;
  --muted:#555;
  --header-bg:#f6efee;
  --hero-blue:#2a78c4;
  --band-blue:#3a3fd0;
  --footer-bg:#eceff4;
  --review-blue:#3d5fa0;
}
*{margin:0;padding:0;box-sizing:border-box}
html,body{width:876px;height:1200px;overflow:hidden;background:#fff}
body{font-family:"Open Sans",Arial,sans-serif;color:var(--text);position:relative}
a{color:var(--link);text-decoration:none}
.topbar{position:absolute;top:0;left:0;width:876px;height:18px;background:var(--navy)}
.topbar .tab{position:absolute;right:0;top:0;height:18px;width:560px;background:var(--navy)}
.toplinks{position:absolute;right:155px;top:3px;display:flex;gap:12px;font-size:8px;color:#fff}
.toplinks span{display:flex;align-items:center;gap:4px}
.header{position:absolute;top:18px;left:0;width:876px;height:83px;background:linear-gradient(#fbf6f5,var(--header-bg))}
.brand{position:absolute;left:154px;top:30px;display:flex;align-items:center;gap:6px;font-size:15px;font-weight:700;color:var(--maroon)}
.brand i{width:12px;height:12px;border-radius:50%;background:var(--navy);display:block}
.call{position:absolute;right:155px;top:8px;text-align:right}
.call .lbl{font-size:10px;font-weight:700;color:#222}
.call .num{font-size:18px;color:var(--red);line-height:22px}
.appt{position:absolute;right:155px;top:52px;width:192px;height:21px;border-radius:11px;background:var(--navy);color:#fff;font-size:9.2px;letter-spacing:.4px;display:flex;align-items:center;gap:8px;padding-left:9px}
.appt b{width:13px;height:11px;background:#e07a22;border-radius:2px;display:block}
.nav{position:absolute;top:101px;left:0;width:876px;height:31px;background:linear-gradient(#9a1f22,#7c1518)}
.nav ul{list-style:none;display:flex;position:absolute;left:158px;top:7px;gap:0}
.nav li{font-size:9.2px;color:#fff;padding:2px 10px;height:18px;line-height:14px}
.nav li.active{background:#fff;color:var(--red);border-radius:3px}
.hero{position:absolute;top:132px;left:0;width:876px;height:236px;background:linear-gradient(90deg,#1d5fae,#4a98d8 20%,#2d6fbe 50%,#4a98d8 80%,#d9e6f3)}
.hero .band{position:absolute;bottom:0;left:0;width:876px;height:8px;background:var(--band-blue)}
.slide{position:absolute;top:146px;left:154px;width:567px;height:233px;border-radius:5px;background:radial-gradient(ellipse at 55% 45%,#e8b596,#b7785a 45%,#5a3424);border:2px solid #fff;box-shadow:0 3px 6px rgba(0,0,0,.35);overflow:hidden}
.caption{position:absolute;left:0;top:148px;width:300px;height:64px;background:linear-gradient(90deg,rgba(30,20,20,.75),rgba(30,20,20,.55) 70%,rgba(30,20,20,0));color:#fff;padding:4px 0 0 22px}
.caption .s{font-size:16px;font-weight:400}
.caption .l{font-size:27px;font-weight:600;line-height:32px}
.dots{position:absolute;top:396px;left:413px;display:flex;gap:9px}
.dots i{width:9px;height:9px;border-radius:50%;background:var(--maroon);display:block}
.dots i.on{background:#fff;border:2px solid var(--maroon)}
.main{position:absolute;top:428px;left:153px;width:380px;font-size:7.6px;line-height:11.8px}
.main p{margin-bottom:11px}
.main ul{list-style:none;margin-bottom:11px}
.main li{position:relative;padding-left:11px;margin-bottom:6.5px}
.main li::before{content:"";position:absolute;left:1px;top:3.5px;width:5px;height:5px;border-radius:50%;background:#999}
.side{position:absolute;top:428px;left:559px;width:163px}
.side h3{font-size:10.5px;color:var(--maroon);font-weight:700;margin-bottom:4px}
.ph{display:block}
.video{height:94px;background:linear-gradient(135deg,#6a7fa0,#c9b8a8 50%,#40507a)}
.vcap{font-size:8px;margin:4px 0 10px}
.card{position:relative;height:94px;margin-bottom:13px;overflow:hidden}
.card.child{background:linear-gradient(90deg,#333 55%,#8a6a58)}
.card.child .q{position:absolute;left:11px;top:7px;color:#fff;font-weight:700;font-size:10.5px;line-height:12.5px}
.card.child .bar{position:absolute;left:0;top:55px;width:163px;height:18px;background:var(--red);color:#fff;font-size:8px;font-weight:700;padding:3px 10px}
.btn{position:absolute;border-radius:8px;background:#2a2a2a;color:#fff;font-size:6.8px;padding:2px 8px;letter-spacing:.3px}
.card.success{background:linear-gradient(90deg,#fff 55%,#f1e6d8);border:1px solid #ccc}
.card.success .t{position:absolute;left:7px;top:20px;font-size:11.5px;font-weight:700;color:var(--red);line-height:14px}
.card.success .ph{position:absolute;right:0;top:0;width:65px;height:94px;background:linear-gradient(#f3d9bc,#c99a6f)}
.reviews{height:80px;border-radius:4px;background:linear-gradient(#5276b8,var(--review-blue));color:#fff;text-align:center;margin-bottom:13px;padding-top:10px}
.reviews .t{font-size:13px}
.reviews svg{margin:4px 0 2px}
.reviews .p{font-size:7px}
.fb{height:158px;border:1px solid #ccc;font-size:6.6px;padding:3px 4px;color:#333}
.fb .hd{font-weight:700;border-bottom:1px solid #ddd;padding-bottom:3px;margin-bottom:5px}
.fb .pg{display:flex;gap:5px;margin-bottom:5px}
.fb .av{width:26px;height:26px;background:#b49a88}
.fb .nm{color:#3b5998;font-weight:700;font-size:7px}
.fb .like{display:inline-block;margin-top:2px;background:#4a66a0;color:#fff;padding:0 4px;font-size:6px}
.fb .grid{display:grid;grid-template-columns:repeat(5,26px);gap:3px;margin:5px 0 6px 4px}
.fb .grid i{height:26px;display:block;background:#9aa4b0}
.fb .grid i:nth-child(odd){background:#c2a48c}
.fb .ft{color:#888;font-size:5.5px}
.footer{position:absolute;top:1053px;left:0;width:876px;height:147px;background:var(--footer-bg)}
.fbrand{position:absolute;left:154px;top:28px;display:flex;align-items:center;gap:6px;font-size:13px;font-weight:700;color:var(--maroon)}
.fbrand i{width:10px;height:10px;border-radius:50%;background:var(--navy);display:block}
.fname{position:absolute;left:313px;top:14px}
.fname .a{font-size:11px;font-weight:700;color:#333}
.fname .b{font-size:10px;font-weight:600;font-style:italic;color:var(--navy);margin-top:1px}
.addr{position:absolute;top:58px;font-size:7.6px;line-height:11.8px;color:#222}
.addr b{color:var(--red)}
.addr1{left:313px}
.addr2{left:429px;border-left:1px dashed #aaa;padding-left:0;height:72px}
.addr2 div{margin-left-:0;padding-left:0}
.flinks{position:absolute;top:16px;list-style:none;font-size:8.2px;color:#333}
.flinks li{margin-bottom:7px;line-height:10px}
.flinks li::before{content:"› ";color:#333}
.fl1{left:560px}
.fl2{left:649px;width:80px}
.copy{position:absolute;top:1186px;left:0;width:876px;text-align:center;font-size:7px;color:#555}
</style>
</head>
<body>
<div class="topbar">
  <div class="toplinks">
    <span><svg width="9" height="8" viewBox="0 0 9 8"><path d="M4.5 0 9 4H7.5v4h-2V5.5h-2V8h-2V4H0z" fill="#fff"/></svg>Home</span>
    <span><svg width="9" height="7" viewBox="0 0 9 7"><rect width="9" height="7" fill="#fff"/><path d="M0 0l4.5 3.5L9 0" stroke="#1b1f5e" fill="none"/></svg>Contact Us</span>
  </div>
</div>
<header class="header">
  <div class="brand"><i></i>Clearpath Vision Centers</div>
  <div class="call"><div class="lbl">Call Us Now</div><div class="num">410-555-0142</div></div>
  <div class="appt"><b></b>REQUEST FOR AN APPOINTMENT</div>
</header>
<nav class="nav"><ul>
  <li class="active">Meet Us</li><li>New Patients</li><li>Vision &amp; Learning</li><li>Vision Therapy</li><li>Binocular Vision Disorders</li><li>Head Injuries</li><li>Professionals</li>
</ul></nav>
<section class="hero" role="img" aria-label="Blue clinic backdrop with an eye chart"><div class="band"></div></section>
<div class="slide" role="img" aria-label="Photo of a smiling child looking through a trial frame during an eye exam">
  <div class="caption"><div class="s">Improving Vision,</div><div class="l">Changing Lives</div></div>
</div>
<div class="dots"><i class="on"></i><i></i><i></i><i></i></div>

<main class="main">
  <p>There are many visual skills critical for reading and learning. Often, a vision problem is misdiagnosed as an attention problem or a learning disability due to similarity of symptoms. Anyone who is struggling with reading, has poor reading comprehension, or just isn't performing to their full potential, should consider scheduling a developmental vision evaluation. To help determine if you or your child should be tested, <a>Do the Checklist</a> on our <a>Vision Quiz page</a>.</p>
  <p><a>Dr. Daniel Harlow</a> is a developmental optometrist who specializes in the diagnosis and treatment of vision problems that interfere with reading and learning. He is a member of the National Optometric Society, the Guild of Vision Development Clinicians, and a Fellow in the National Academy of Eye Care.</p>
  <p>Clearpath Vision Centers and Dr. Daniel Harlow provide:</p>
  <ul>
    <li>Comprehensive <a>Eye Examinations</a> for All Ages, including Infants and Preschoolers</li>
    <li><a>Vision Therapy</a> for All Ages</li>
    <li>Treatment for <a>Learning-related Vision Problems</a></li>
    <li>Free Monthly Seminars. Visit our Friendlink page for information about our free monthly seminars on a variety of topics, including: <a>The Hidden Disability - Undiagnosed Vision Problems</a>.</li>
    <li>Continuing Education seminars for Optometrists, Occupational Therapists and Physical Therapists. All CE offerings are free and board approved. For CE information and dates, see our <a>success stories, blogs and videos on Binocular Vision Disorders</a></li>
    <li>Treatment for <a>Binocular Vision Conditions</a>, such as <a>Amblyopia or Lazy Eye</a>, <a>Convergence Insufficiency</a> <i>(near vision disorder)</i>, <a>Diplopia</a> <i>(double vision)</i>, <a>Lack of Stereopsis</a> <i>(two-eyed depth perception)</i>, and <a>Strabismus</a> <i>(cross-eyed, wandering eye, eye turns, etc.)</i></li>
    <li><a>Visual Rehabilitation for Patients with Special Needs, such as Developmental Delays or Traumatic Brain Injury</a> (TBI), including Autism, Stroke, Whiplash, CP, MS, etc.</li>
    <li>Treatment for <a>Stress-related Visual Problems</a>, including Blurred Vision, Visual Stress from Reading and Computers, Eye Strain Headaches, and/or Vision-induced Stomachaches or Motion Sickness</li>
    <li><a>Sports Vision</a> Correction and/or Improvement</li>
  </ul>
  <p>At vero eos et accusamus et iusto odio dignissimos ducimus qui blanditiis praesentium voluptatum deleniti atque corrupti quos dolores et quas molestias excepturi sint occaecati cupiditate non provident, similique sunt in culpa qui officia deserunt mollitia animi, id est laborum et dolorum fuga. Et harum quidem rerum facilis est et expedita distinctio. Nam libero tempore, cum soluta nobis est eligendi optio cumque nihil impedit quo minus id quod maxime placeat facere possimus, omnis voluptas assumenda est, omnis dolor repellendus. Temporibus autem quibusdam et aut officiis debitis aut rerum necessitatibus saepe eveniet ut et voluptates repudiandae sint et molestiae non recusandae. Itaque earum rerum hic tenetur a sapiente delectus, ut aut reiciendis voluptatibus maiores alias consequatur aut perferendis doloribus asperiores repellat.</p>
  <p>Sed ut perspiciatis unde omnis iste natus error sit voluptatem accusantium doloremque laudantium, totam rem aperiam, eaque ipsa quae ab illo inventore veritatis et quasi architecto beatae vitae dicta sunt explicabo. Nemo enim ipsam voluptatem quia voluptas sit aspernatur aut odit aut fugit, sed quia consequuntur magni dolores eos qui ratione voluptatem sequi nesciunt. Neque porro quisquam est, qui dolorem ipsum quia dolor sit amet, consectetur, adipisci velit, sed quia non numquam eius modi tempora incidunt ut labore et dolore magnam aliquam quaerat voluptatem. Ut enim ad minima veniam, quis nostrum exercitationem ullam corporis suscipit laboriosam, nisi ut aliquid ex ea commodi consequatur?</p>
</main>

<aside class="side">
  <h3>Featured Video</h3>
  <div class="ph video" role="img" aria-label="Video still of the doctor in a news interview"></div>
  <div class="vcap">Channel 9 News</div>
  <div class="card child" role="img" aria-label="Child at a chalkboard">
    <div class="q">Does my child<br>have a vision<br>problem?</div>
    <div class="bar">or Symptoms of a Vision Problem</div>
    <div class="btn" style="right:6px;top:76px">READ MORE ›</div>
  </div>
  <div class="card success">
    <div class="t">Success with<br>Vision Therapy</div>
    <div class="btn" style="left:8px;top:53px">READ MORE ›</div>
    <div class="ph" role="img" aria-label="Girl in glasses reading a book"></div>
  </div>
  <div class="reviews">
    <div class="t">Read Our Reviews »</div>
    <svg width="90" height="16" viewBox="0 0 90 16">
      <g fill="#f7d84a" stroke="#fff" stroke-width=".6">
        <path id="st" d="M8 0.5l2.2 4.8 5.2.5-3.9 3.5 1.2 5.1L8 11.7l-4.7 2.7 1.2-5.1L.6 5.8l5.2-.5z"/>
        <use href="#st" x="18"/><use href="#st" x="36"/><use href="#st" x="54"/><use href="#st" x="72"/>
      </g>
    </svg>
    <div class="p">powered by Reviewly</div>
  </div>
  <div class="fb">
    <div class="hd">Find us on Friendlink</div>
    <div class="pg"><div class="av" role="img" aria-label="Doctor profile photo"></div><div><div class="nm">Clearpath: Dr. Daniel Harlow, Developmental Optometrist</div><span class="like">Like</span></div></div>
    <div>155 people like <span style="color:#3b5998">Clearpath: Dr. Daniel Harlow, Developmental Optometrist.</span></div>
    <div class="grid" role="img" aria-label="Follower profile photos"><i></i><i></i><i></i><i></i><i></i><i></i><i></i><i></i><i></i><i></i></div>
    <div class="ft">Friendlink social plugin</div>
  </div>
</aside>

<footer class="footer">
  <div class="fbrand"><i></i>Clearpath Vision</div>
  <div class="fname"><div class="a">Clearpath Vision Centers</div><div class="b">Dr. Daniel Harlow</div></div>
  <div class="addr addr1">4120 Meadowbrook Pkwy.<br>Ridgeview Center, Ste. 6<br>Linden, MD, 21090<br><b>Phone:</b> <strong>410-555-0142</strong><br>Fax: 410-555-0143</div>
  <div class="addr addr2"><div style="padding-left:0;margin-left:0"><span style="display:block;padding-left:0"></span></div></div>
  <div class="addr" style="left:429px">57 Harbor Lane Suite 300,<br>Room 2<br>Fairhaven, MD, 21099<br><b>Phone:</b> <strong>410-555-0142</strong></div>
  <ul class="flinks fl1"><li>Home</li><li>Meet Us</li><li>New Patients</li><li>Vision &amp; Learning</li><li>Vision Therapy</li></ul>
  <ul class="flinks fl2"><li>Binocular Vision<br>&nbsp;&nbsp;Disorders</li><li>Head Injuries</li><li>Professionals</li><li>Contact Us</li></ul>
</footer>
<div class="copy">Copyright © 2014 Clearpath Vision Centers, Inc. All rights reserved.</div>
</body>
</html>
```